Halvex Therapeutics is a biotech company that needs a powerpoint theme.

We need a powerpoint theme with several different slide templates we could use for presentation of data or research ideas. Our logo is attached. We picked "Halvex" as our company name because we use epigenome editing tools to fine-tune gene expression for therapeutic purposes. Our logo color is a seafoam green, and we would like to see this color along with other colors that could complement it well. Keywords: genetics, biotech, cells, human therapies,

```html
<!DOCTYPE html>
<html lang="en">
<head>
<meta charset="utf-8">
<title>Halvex Therapeutics – Presentation Theme</title>
<link href="https://fonts.googleapis.com/css2?family=Exo+2:wght@300;400&family=Montserrat:wght@400;500&display=swap" rel="stylesheet">
<style>
  :root{
    --seafoam:#35d6c2; --seafoam-deep:#14a08c; --mint:#8ef0e0; --mint-soft:#c6f5ee;
    --blue:#1e84d9; --royal:#2f6ff0; --violet:#6a2ee0; --magenta:#b23de6;
    --ink:#2f3437; --grey:#8a9095; --line:#e6eceb; --paper:#ffffff;
  }
  html,body{margin:0;padding:0;width:900px;height:1200px;overflow:hidden;background:var(--paper);}
  .theme-board{
    width:900px;height:1200px;box-sizing:border-box;padding:33px 0 0 22px;
    display:grid;grid-template-columns:repeat(3,259px);grid-auto-rows:146px;column-gap:39px;row-gap:18.6px;
  }
  .slide{width:259px;height:146px;display:block;background:var(--paper);box-shadow:0 6px 18px rgba(20,60,60,.16);overflow:hidden;}
  .defs{position:absolute;width:0;height:0;}
  .ttl{font-family:"Exo 2",sans-serif;font-weight:300;font-size:20px;fill:var(--ink);}
  .ttl-sm{font-family:"Exo 2",sans-serif;font-weight:300;font-size:14px;fill:var(--ink);}
  .lab-ttl{font-family:"Exo 2",sans-serif;font-weight:300;font-size:18px;fill:var(--ink);}
  .sub{font-family:Montserrat,sans-serif;font-size:4.5px;fill:var(--ink);}
  .body{font-family:Montserrat,sans-serif;font-size:4.2px;fill:var(--grey);}
  .tiny{font-family:Montserrat,sans-serif;font-size:3.4px;fill:var(--grey);}
  .label{font-family:Montserrat,sans-serif;font-size:7px;fill:var(--ink);}
  .label-s{font-family:Montserrat,sans-serif;font-size:5.5px;fill:var(--ink);}
  .stat{font-family:"Exo 2",sans-serif;font-weight:400;font-size:15px;fill:var(--royal);}
  .side{font-family:Montserrat,sans-serif;font-size:6.5px;letter-spacing:.5px;fill:var(--ink);}
  .white{fill:#fff;}
  .center{text-anchor:middle;}
  .end{text-anchor:end;}
  .brand-name{font-family:"Exo 2",sans-serif;font-weight:400;fill:currentColor;letter-spacing:2px;}
  .brand-mark{fill:none;stroke:currentColor;stroke-width:2.2;}
  .logo-teal{color:var(--seafoam);}
  .logo-white{color:#fff;}
  .icon{fill:none;stroke:var(--seafoam-deep);stroke-width:1.4;stroke-linecap:round;stroke-linejoin:round;}
</style>
</head>
<body>

<svg class="defs" aria-hidden="true">
  <defs>
    <linearGradient id="g-lab" x1="0" y1="0" x2="1" y2="1">
      <stop offset="0" stop-color="#e6f1f1"/><stop offset=".45" stop-color="#9dd6d0"/>
      <stop offset=".75" stop-color="#e9a970"/><stop offset="1" stop-color="#c4def0"/>
    </linearGradient>
    <linearGradient id="g-glove" x1="0" y1="0" x2="1" y2="1">
      <stop offset="0" stop-color="#2a4fb3"/><stop offset=".55" stop-color="#6c9ae6"/><stop offset="1" stop-color="#f26b4c"/>
    </linearGradient>
    <linearGradient id="g-petri" x1="0" y1="0" x2="0" y2="1">
      <stop offset="0" stop-color="#e7e3d0"/><stop offset=".6" stop-color="#8a64dc"/><stop offset="1" stop-color="#eeeef6"/>
    </linearGradient>
    <linearGradient id="g-deep" x1="0" y1="0" x2="1" y2="1">
      <stop offset="0" stop-color="#0d2b66"/><stop offset=".6" stop-color="#2d70d2"/><stop offset="1" stop-color="#a8dcf2"/>
    </linearGradient>
    <linearGradient id="g-coat" x1="0" y1="0" x2="0" y2="1">
      <stop offset="0" stop-color="#dfe9f3"/><stop offset="1" stop-color="#f8fbfd"/>
    </linearGradient>
    <linearGradient id="g-cover" x1="0" y1="0" x2="1" y2="1">
      <stop offset="0" stop-color="#62ddcc"/><stop offset="1" stop-color="#2fcbb6"/>
    </linearGradient>
    <clipPath id="flask-inner"><path d="M101 118 L42 238 H181 L122 118Z"/></clipPath>

    <symbol id="logo" viewBox="0 0 100 26">
      <circle class="brand-mark" cx="12" cy="13" r="10"/>
      <text class="brand-name" x="28" y="17" font-size="13">HALVEX</text>
    </symbol>

    <symbol id="i-molecule" viewBox="0 0 24 24">
      <g class="icon"><circle cx="6" cy="6" r="3"/><circle cx="18" cy="7" r="3"/><circle cx="12" cy="18" r="3.5"/><path d="M8.5 7.5 L10.5 15 M15.5 8.5 L13.5 15 M9 6 H15"/></g>
    </symbol>
    <symbol id="i-flask" viewBox="0 0 24 24">
      <g class="icon"><path d="M9 3 H15 M10 3 V10 L4 20 H20 L14 10 V3"/><path d="M7 15 H17"/></g>
    </symbol>
    <symbol id="i-cell" viewBox="0 0 24 24">
      <g class="icon"><circle cx="12" cy="12" r="9"/><circle cx="12" cy="12" r="3.5"/><circle cx="6.5" cy="9" r="1"/><circle cx="17" cy="16" r="1"/></g>
    </symbol>
    <symbol id="i-helix" viewBox="0 0 24 24">
      <g class="icon"><path d="M7 3 C17 8 7 16 17 21 M17 3 C7 8 17 16 7 21 M9 7 H15 M9 12 H15 M9 17 H15"/></g>
    </symbol>
    <symbol id="i-person" viewBox="0 0 24 24">
      <g class="icon"><circle cx="12" cy="7" r="4"/><path d="M4 21 C4 15 20 15 20 21Z"/></g>
    </symbol>
  </defs>
</svg>

<main class="theme-board">

  <!-- 1 Cover -->
  <svg class="slide cover" viewBox="0 0 478 269">
    <rect width="478" height="269" fill="var(--seafoam)"/>
    <rect width="478" height="269" fill="url(#g-cover)" opacity=".8" role="img" aria-label="Laboratory bench with glassware under a seafoam tint"/>
    <circle cx="172" cy="132" r="26" fill="none" stroke="#fff" stroke-width="4"/>
    <text class="brand-name" x="212" y="140" font-size="30" fill="#fff" style="color:#fff">HALVEX</text>
    <text class="brand-name" x="214" y="152" font-size="8" style="color:#fff;letter-spacing:4px">THERAPEUTICS</text>
  </svg>

  <!-- 2 About -->
  <svg class="slide about" viewBox="0 0 478 269">
    <rect width="478" height="269" fill="url(#g-lab)" role="img" aria-label="Microscope and colourful test tubes on a lab bench"/>
    <path d="M0 0 H215 A175 175 0 0 1 215 269 H0Z" fill="var(--seafoam)"/>
    <use href="#logo" x="58" y="92" width="110" height="28" class="logo-white"/>
    <text class="tiny white" x="60" y="140"><tspan x="60">Our mission is to give medicine precise control over</tspan><tspan x="60" dy="7">gene activity. We pair epigenome editing with careful</tspan><tspan x="60" dy="7">biology to build therapies that switch disease genes</tspan><tspan x="60" dy="7">down or up, without altering the DNA sequence, and</tspan><tspan x="60" dy="7">that last for years after a single treatment.</tspan></text>
    <text class="side white" transform="rotate(-90 26 210)" x="26" y="210">ABOUT</text>
  </svg>

  <!-- 3 Bullet slide -->
  <svg class="slide bullets" viewBox="0 0 478 269">
    <circle cx="34" cy="122" r="46" fill="var(--mint-soft)"/>
    <circle cx="492" cy="122" r="52" fill="var(--mint-soft)"/>
    <circle cx="358" cy="124" r="63" fill="url(#g-petri)" role="img" aria-label="Purple solution in a petri dish with a pipette"/>
    <use href="#logo" x="373" y="10" width="90" height="24" class="logo-teal"/>
    <text class="ttl" x="106" y="90">BULLET SLIDE</text>
    <g class="tiny">
      <text x="114" y="110"><tspan x="114">Define the target gene and the tissue where the change</tspan><tspan x="114" dy="5">must happen, then rank options by safety and need.</tspan></text>
      <text x="114" y="128"><tspan x="114">Screen guide designs in human cells and keep only those</tspan><tspan x="114" dy="5">with strong, stable and specific repression results.</tspan></text>
      <text x="114" y="146"><tspan x="114">Tune delivery and dose in models that match patients,</tspan><tspan x="114" dy="5">tracking durability of the effect over many months.</tspan></text>
      <text x="114" y="164"><tspan x="114">Share results with clinical partners early so that</tspan><tspan x="114" dy="5">trial plans reflect what the biology has shown us.</tspan></text>
    </g>
    <g fill="var(--seafoam)"><circle cx="109" cy="109" r="1"/><circle cx="109" cy="127" r="1"/><circle cx="109" cy="145" r="1"/><circle cx="109" cy="163" r="1"/></g>
  </svg>

  <!-- 4 Title text, blue -->
  <svg class="slide title-blue" viewBox="0 0 478 269">
    <rect width="478" height="269" fill="var(--blue)"/>
    <circle cx="140" cy="134" r="118" fill="#1c77c6"/>
    <circle cx="140" cy="134" r="98" fill="#1a68b2"/>
    <circle cx="140" cy="134" r="84" fill="url(#g-deep)" role="img" aria-label="Gloved hand adding dye to test tubes"/>
    <use href="#logo" x="373" y="10" width="90" height="24" class="logo-teal"/>
    <text class="ttl white" x="268" y="106">TITLE TEXT</text>
    <text class="tiny white" x="282" y="130"><tspan x="282">Each program starts with a clear view of the disease</tspan><tspan x="282" dy="7">gene and the cells where it acts, then builds upward</tspan><tspan x="282" dy="7">toward a single, durable treatment.</tspan></text>
    <text class="tiny white" x="282" y="162"><tspan x="282">Results from every study return to the design team</tspan><tspan x="282" dy="7">so each new editor is sharper and more specific than</tspan><tspan x="282" dy="7">the one that came before it.</tspan></text>
    <g fill="#fff"><circle cx="277" cy="129" r="1"/><circle cx="277" cy="161" r="1"/></g>
  </svg>

  <!-- 5 Focus areas -->
  <svg class="slide focus" viewBox="0 0 478 269">
    <rect width="478" height="269" fill="var(--mint-soft)" role="img" aria-label="Faint laboratory glassware in mint tones"/>
    <circle cx="432" cy="134" r="272" fill="#fff"/>
    <use href="#logo" x="16" y="118" width="134" height="34" class="logo-teal"/>
    <g class="center">
      <text class="ttl-sm" x="328" y="52">GENETICS</text>
      <text class="tiny" x="328" y="61"><tspan x="328">Mapping how genes are switched on and off across</tspan><tspan x="328" dy="5">healthy and diseased human tissue.</tspan></text>
      <text class="ttl-sm" x="328" y="104">BIOTECH</text>
      <text class="tiny" x="328" y="113"><tspan x="328">Engineering compact editors and delivery systems</tspan><tspan x="328" dy="5">built for reliable manufacture.</tspan></text>
      <text class="ttl-sm" x="328" y="163">EPIGENOME</text>
      <text class="tiny" x="328" y="172"><tspan x="328">Writing lasting marks that hold gene activity at</tspan><tspan x="328" dy="5">the level a patient needs.</tspan></text>
      <text class="ttl-sm" x="328" y="215">CELLS</text>
      <text class="tiny" x="328" y="224"><tspan x="328">Testing every design in primary human cells before</tspan><tspan x="328" dy="5">it moves into models.</tspan></text>
    </g>
  </svg>

  <!-- 6 Statement -->
  <svg class="slide statement" viewBox="0 0 478 269">
    <rect width="478" height="269" fill="var(--mint-soft)"/>
    <circle cx="-4" cy="134" r="154" fill="url(#g-lab)" role="img" aria-label="Lab stand with coloured flasks"/>
    <circle cx="484" cy="130" r="42" fill="url(#g-lab)" role="img" aria-label="Test tubes in a rack"/>
    <use href="#logo" x="373" y="10" width="90" height="24" class="logo-teal"/>
    <g class="center" style="font-family:'Exo 2',sans-serif;font-weight:300;font-size:18px;fill:var(--ink)">
      <text x="282" y="90">We use epigenome</text>
      <text x="282" y="116">editing tools to fine-</text>
      <text x="282" y="142">tune gene expression</text>
      <text x="282" y="168">for therapeutic</text>
      <text x="282" y="194">purposes.</text>
    </g>
  </svg>

  <!-- 7 Our services -->
  <svg class="slide services" viewBox="0 0 478 269">
    <circle cx="115" cy="134" r="72" fill="#fff" stroke="var(--line)" stroke-width="1.5"/>
    <circle cx="115" cy="134" r="60" fill="url(#g-glove)" role="img" aria-label="Gloved hand holding a sample plate"/>
    <text class="side" transform="rotate(-90 27 210)" x="27" y="210">OUR SERVICES</text>
    <line x1="22" y1="218" x2="22" y2="269" stroke="var(--ink)" stroke-width=".8"/>
    <use href="#logo" x="373" y="10" width="90" height="24" class="logo-teal"/>
    <use href="#i-molecule" x="238" y="52" width="26" height="26"/>
    <use href="#i-cell" x="356" y="52" width="26" height="26"/>
    <use href="#i-flask" x="238" y="150" width="26" height="26"/>
    <use href="#i-person" x="356" y="150" width="26" height="26"/>
    <text class="label-s" x="240" y="94">GENETICS</text>
    <text class="label-s" x="358" y="94">BIOTECH</text>
    <text class="label-s" x="240" y="192">CELLS</text>
    <text class="label-s" x="358" y="192">HUMAN THERAPIES</text>
    <g class="tiny">
      <text x="240" y="101"><tspan x="240">Target discovery from tissue</tspan><tspan x="240" dy="4.5">maps and patient data sets.</tspan><tspan x="240" dy="4.5">Ranked by need.</tspan></text>
      <text x="358" y="101"><tspan x="358">Editor design, delivery and</tspan><tspan x="358" dy="4.5">scale-up under one roof.</tspan><tspan x="358" dy="4.5">Built to last.</tspan></text>
      <text x="240" y="199"><tspan x="240">Screens in primary human</tspan><tspan x="240" dy="4.5">cells with deep read-outs.</tspan><tspan x="240" dy="4.5">Fast cycles.</tspan></text>
      <text x="358" y="199"><tspan x="358">Programs shaped with care</tspan><tspan x="358" dy="4.5">teams from the first day.</tspan><tspan x="358" dy="4.5">Patient first.</tspan></text>
    </g>
  </svg>

  <!-- 8 SWOT -->
  <svg class="slide swot" viewBox="0 0 478 269">
    <rect width="478" height="269" fill="var(--seafoam-deep)"/>
    <circle cx="239" cy="134" r="98" fill="#189684"/>
    <circle cx="239" cy="134" r="74" fill="#138a78"/>
    <circle cx="206" cy="103" r="32" fill="#17a78f"/>
    <circle cx="270" cy="103" r="32" fill="var(--royal)"/>
    <circle cx="206" cy="167" r="32" fill="var(--royal)"/>
    <circle cx="270" cy="167" r="32" fill="#17a78f"/>
    <g class="center" style="font-family:'Exo 2',sans-serif;font-size:15px;fill:#fff">
      <text x="206" y="108">S</text><text x="270" y="108">W</text><text x="206" y="172">T</text><text x="270" y="172">O</text>
    </g>
    <use href="#logo" x="373" y="10" width="90" height="24" class="logo-white"/>
    <text class="side white" transform="rotate(-90 26 215)" x="26" y="215">SWOT ANALYSIS</text>
    <g class="tiny end" style="fill:#dff8f3">
      <text class="label-s end" style="fill:#fff" x="154" y="92">Strengths</text>
      <text x="154" y="100"><tspan x="154">Proven editors with long effect</tspan><tspan x="154" dy="4.5">in human cells and models, and a</tspan><tspan x="154" dy="4.5">team that spans biology and</tspan><tspan x="154" dy="4.5">clinic from the start.</tspan></text>
      <text class="label-s end" style="fill:#fff" x="154" y="160">Threats</text>
      <text x="154" y="168"><tspan x="154">Fast moving rivals, shifting</tspan><tspan x="154" dy="4.5">rules for new gene medicines and</tspan><tspan x="154" dy="4.5">long timelines before the first</tspan><tspan x="154" dy="4.5">patient data arrive.</tspan></text>
    </g>
    <g class="tiny" style="fill:#dff8f3">
      <text class="label-s" style="fill:#fff" x="324" y="92">Weaknesses</text>
      <text x="324" y="100"><tspan x="324">Delivery beyond the liver is</tspan><tspan x="324" dy="4.5">still early, and manufacturing at</tspan><tspan x="324" dy="4.5">scale needs new partners and</tspan><tspan x="324" dy="4.5">added funding.</tspan></text>
      <text class="label-s" style="fill:#fff" x="324" y="160">Opportunities</text>
      <text x="324" y="168"><tspan x="324">Many diseases need a dial, not</tspan><tspan x="324" dy="4.5">a cut. One platform can serve</tspan><tspan x="324" dy="4.5">dozens of programs across</tspan><tspan x="324" dy="4.5">organs and ages.</tspan></text>
    </g>
  </svg>

  <!-- 9 Title + four images -->
  <svg class="slide title-grid" viewBox="0 0 478 269">
    <use href="#logo" x="373" y="10" width="90" height="24" class="logo-teal"/>
    <text class="ttl" x="32" y="88">TITLE TEXT HERE</text>
    <text class="body" x="32" y="112"><tspan x="32">Our platform maps chromatin marks across each tissue we study,</tspan><tspan x="32" dy="7.2">building a clear picture of how genes switch on and off. Every</tspan><tspan x="32" dy="7.2">program starts with a careful screen of candidate targets, then</tspan><tspan x="32" dy="7.2">guide design, delivery tuning and dose studies in human cells.</tspan><tspan x="32" dy="7.2">Results feed straight back into the next design round, so each</tspan><tspan x="32" dy="7.2">cycle is faster and more precise. We share key methods with</tspan><tspan x="32" dy="7.2">partners to move the field forward, and clinical teams join the</tspan><tspan x="32" dy="7.2">work early to shape endpoints and safety plans from day one.</tspan></text>
    <rect x="268" y="52" width="78" height="78" fill="url(#g-petri)" role="img" aria-label="Petri dish with purple solution"/>
    <rect x="356" y="52" width="78" height="78" fill="url(#g-glove)" role="img" aria-label="Gloved hand with a sample plate"/>
    <rect x="268" y="140" width="78" height="78" fill="url(#g-lab)" role="img" aria-label="Microscope beside coloured test tubes"/>
    <rect x="356" y="140" width="78" height="78" fill="url(#g-deep)" role="img" aria-label="Researcher at a lab bench in blue light"/>
  </svg>

  <!-- 10 Image left + title -->
  <svg class="slide image-left" viewBox="0 0 478 269">
    <rect x="12" y="12" width="203" height="245" fill="url(#g-lab)" role="img" aria-label="Microscope and test tubes in front of a city window"/>
    <use href="#logo" x="373" y="10" width="90" height="24" class="logo-teal"/>
    <text class="ttl" x="240" y="84">TITLE TEXT HERE</text>
    <text class="body" x="240" y="108"><tspan x="240">Our platform maps chromatin marks across each</tspan><tspan x="240" dy="7.2">tissue we study, building a clear picture of how genes</tspan><tspan x="240" dy="7.2">switch on and off. Each program starts with a careful</tspan><tspan x="240" dy="7.2">screen of targets, then guide design and dose studies.</tspan><tspan x="240" dy="7.2">Results feed back into the next design round, so every</tspan><tspan x="240" dy="7.2">cycle is faster and more precise than the last one.</tspan><tspan x="240" dy="7.2">Clinical teams join early to shape endpoints and safety</tspan><tspan x="240" dy="7.2">plans, keeping patients at the centre of the work.</tspan></text>
  </svg>

  <!-- 11 Title + image right -->
  <svg class="slide image-right" viewBox="0 0 478 269">
    <use href="#logo" x="30" y="10" width="90" height="24" class="logo-teal"/>
    <text class="ttl" x="32" y="88">TITLE TEXT DEMO</text>
    <text class="body" x="32" y="112"><tspan x="32">Our platform maps chromatin marks across each tissue we study,</tspan><tspan x="32" dy="7.2">building a clear picture of how genes switch on and off. Every</tspan><tspan x="32" dy="7.2">program starts with a careful screen of candidate targets, then</tspan><tspan x="32" dy="7.2">guide design, delivery tuning and dose studies in human cells.</tspan><tspan x="32" dy="7.2">Results feed straight back into the next design round, so each</tspan><tspan x="32" dy="7.2">cycle is faster and more precise. We share key methods with</tspan><tspan x="32" dy="7.2">partners to move the field forward, and clinical teams join the</tspan><tspan x="32" dy="7.2">work early to shape endpoints and safety plans from day one.</tspan></text>
    <rect x="263" y="12" width="204" height="245" fill="url(#g-petri)" role="img" aria-label="Pipette dropping purple liquid into a petri dish"/>
  </svg>

  <!-- 12 Three images & text -->
  <svg class="slide three-images" viewBox="0 0 478 269">
    <use href="#logo" x="30" y="10" width="90" height="24" class="logo-teal"/>
    <text class="ttl" x="32" y="85">THREE IMAGES</text>
    <text class="ttl" x="32" y="112">&amp; TEXT</text>
    <text class="tiny" x="32" y="136"><tspan x="32">Our platform maps chromatin marks across each tissue we study, building</tspan><tspan x="32" dy="6.5">a clear picture of how genes switch on and off. Each program starts with</tspan><tspan x="32" dy="6.5">a careful screen of targets, then guide design and dose studies in cells.</tspan><tspan x="32" dy="6.5">Results feed back into the next round, so each cycle is more precise.</tspan><tspan x="32" dy="6.5">Clinical teams join early to shape endpoints and safety plans, keeping</tspan><tspan x="32" dy="6.5">the patient at the centre of every decision we make.</tspan></text>
    <circle cx="373" cy="84" r="44" fill="url(#g-deep)" role="img" aria-label="Researcher at a microscope"/>
    <circle cx="290" cy="147" r="45" fill="url(#g-glove)" role="img" aria-label="Gloved hand with a sample plate"/>
    <circle cx="374" cy="192" r="45" fill="url(#g-deep)" role="img" aria-label="Gel being loaded with a pipette"/>
  </svg>

  <!-- 13 Team -->
  <svg class="slide team" viewBox="0 0 478 269">
    <rect width="478" height="269" fill="var(--mint)"/>
    <use href="#logo" x="373" y="10" width="90" height="24" class="logo-teal"/>
    <text class="side" transform="rotate(-90 26 205)" x="26" y="205">TEAM</text>
    <line x1="22" y1="215" x2="22" y2="269" stroke="var(--ink)" stroke-width=".8"/>
    <circle cx="105" cy="118" r="45" fill="url(#g-coat)" role="img" aria-label="Portrait of team member in a lab coat"/>
    <circle cx="238" cy="118" r="45" fill="url(#g-coat)" role="img" aria-label="Portrait of team member at a lab bench"/>
    <circle cx="372" cy="118" r="45" fill="url(#g-coat)" role="img" aria-label="Portrait of team member with lab glassware"/>
    <g class="center">
      <text class="label-s" x="105" y="188">Mara Lindqvist</text><text class="tiny" x="105" y="194">Co-founder / CEO</text>
      <text class="label-s" x="238" y="188">John Doe</text><text class="tiny" x="238" y="194">Developer</text>
      <text class="label-s" x="372" y="188">Owen Hale</text><text class="tiny" x="372" y="194">Developer</text>
    </g>
    <g fill="#2a4fd6">
      <circle cx="91" cy="208" r="6"/><circle cx="105" cy="208" r="6"/><circle cx="119" cy="208" r="6"/>
      <circle cx="224" cy="208" r="6"/><circle cx="238" cy="208" r="6"/><circle cx="252" cy="208" r="6"/>
      <circle cx="358" cy="208" r="6"/><circle cx="372" cy="208" r="6"/><circle cx="386" cy="208" r="6"/>
    </g>
  </svg>

  <!-- 14 Portfolio -->
  <svg class="slide portfolio" viewBox="0 0 478 269">
    <circle cx="93" cy="48" r="70" fill="url(#g-petri)" role="img" aria-label="Petri dish with purple solution"/>
    <circle cx="198" cy="123" r="35" fill="url(#g-lab)" role="img" aria-label="Microscope and test tubes"/>
    <circle cx="55" cy="182" r="35" fill="url(#g-deep)" role="img" aria-label="Researcher in blue light"/>
    <circle cx="165" cy="222" r="58" fill="url(#g-glove)" role="img" aria-label="Gloved hand with a sample plate"/>
    <g class="tiny" style="font-size:4.6px">
      <text x="94" y="130">1. Process A</text><text x="215" y="162">2. Process B</text>
      <text x="52" y="219">3. Process C</text><text x="238" y="239">4. Process D</text>
    </g>
    <use href="#logo" x="373" y="10" width="90" height="24" class="logo-teal"/>
    <text class="ttl" x="290" y="98">PORTFOLIO</text>
    <g class="tiny">
      <text x="290" y="118"><tspan x="290">1.  Liver program for a rare metabolic</tspan><tspan x="300" dy="5">disease, now in dose studies.</tspan></text>
      <text x="290" y="136"><tspan x="290">2.  Cardiac target with strong human</tspan><tspan x="300" dy="5">genetics behind the approach.</tspan></text>
      <text x="290" y="154"><tspan x="290">3.  Eye program built on local delivery</tspan><tspan x="300" dy="5">and a single, durable treatment.</tspan></text>
      <text x="290" y="172"><tspan x="290">4.  Neuro research with partners, using</tspan><tspan x="300" dy="5">new capsids to reach the brain.</tspan></text>
    </g>
  </svg>

  <!-- 15 Two images & text -->
  <svg class="slide two-images" viewBox="0 0 478 269">
    <use href="#logo" x="30" y="10" width="90" height="24" class="logo-teal"/>
    <text class="ttl" x="32" y="85">TWO IMAGES</text>
    <text class="ttl" x="32" y="112">&amp; TEXT</text>
    <text class="tiny" x="32" y="136"><tspan x="32">Our platform maps chromatin marks across each tissue we study, building</tspan><tspan x="32" dy="6.5">a clear picture of how genes switch on and off. Each program starts with</tspan><tspan x="32" dy="6.5">a careful screen of targets, then guide design and dose studies in cells.</tspan><tspan x="32" dy="6.5">Results feed back into the next round, so each cycle is more precise.</tspan><tspan x="32" dy="6.5">Clinical teams join early to shape endpoints and safety plans, keeping</tspan><tspan x="32" dy="6.5">the patient at the centre of every decision we make.</tspan></text>
    <circle cx="390" cy="100" r="63" fill="url(#g-deep)" role="img" aria-label="Pipette loading a gel"/>
    <circle cx="305" cy="181" r="62" fill="url(#g-glove)" role="img" aria-label="Gloved hand with a sample plate"/>
  </svg>

  <!-- 16 Lab tube: flask -->
  <svg class="slide lab-flask" viewBox="0 0 478 269">
    <text class="lab-ttl" x="32" y="36">Lab Tube</text>
    <text class="sub" x="32" y="47">Put your subtitle here</text>
    <use href="#logo" x="373" y="10" width="90" height="24" class="logo-teal"/>
    <path d="M86 70 H138 V78 H130 V114 L193 246 H30 L93 114 V78 H86Z" fill="var(--seafoam)"/>
    <path d="M112 78 H130 V114 L193 246 H112Z" fill="var(--mint)"/>
    <g clip-path="url(#flask-inner)">
      <rect x="40" y="124" width="72" height="29" fill="#22b6c9"/><rect x="112" y="124" width="72" height="29" fill="#4fd0dd"/>
      <rect x="40" y="153" width="72" height="29" fill="#1e6be0"/><rect x="112" y="153" width="72" height="29" fill="#4b8cf0"/>
      <rect x="40" y="182" width="72" height="28" fill="var(--violet)"/><rect x="112" y="182" width="72" height="28" fill="#8b5cf0"/>
      <rect x="40" y="210" width="72" height="30" fill="#9b35e0"/><rect x="112" y="210" width="72" height="30" fill="#b966f0"/>
    </g>
    <g class="label-s white center" style="font-size:6px">
      <text x="93" y="141">15%</text><text x="88" y="170">20%</text><text x="83" y="199">25%</text><text x="78" y="228">40%</text>
    </g>
    <g fill="none" stroke="#fff" stroke-width="1"><circle cx="125" cy="138" r="4"/><circle cx="130" cy="167" r="4"/><circle cx="135" cy="196" r="4"/><circle cx="140" cy="225" r="4"/></g>
    <g stroke="#bbb" stroke-width=".5" stroke-dasharray="1.5 1.5">
      <line x1="131" y1="138" x2="205" y2="130"/><line x1="136" y1="167" x2="205" y2="158"/><line x1="141" y1="196" x2="205" y2="186"/><line x1="146" y1="225" x2="205" y2="213"/>
    </g>
    <g class="tiny">
      <text x="207" y="130"><tspan class="label-s" style="font-size:4.2px" x="207">Insert Text</tspan><tspan x="207" dy="4.5">Fits any data type, short</tspan><tspan x="207" dy="4">notes read best here.</tspan></text>
      <text x="207" y="158"><tspan class="label-s" style="font-size:4.2px" x="207">Insert Text</tspan><tspan x="207" dy="4.5">Fits any data type, short</tspan><tspan x="207" dy="4">notes read best here.</tspan></text>
      <text x="207" y="186"><tspan class="label-s" style="font-size:4.2px" x="207">Insert Text</tspan><tspan x="207" dy="4.5">Fits any data type, short</tspan><tspan x="207" dy="4">notes read best here.</tspan></text>
      <text x="207" y="213"><tspan class="label-s" style="font-size:4.2px" x="207">Insert Text</tspan><tspan x="207" dy="4.5">Fits any data type, short</tspan><tspan x="207" dy="4">notes read best here.</tspan></text>
    </g>
    <text class="label-s" x="312" y="137">Science Analysis</text>
    <text class="stat" x="315" y="166">77%</text>
    <text class="tiny" x="352" y="155"><tspan x="352">Of samples screened,</tspan><tspan x="352" dy="5">most held the effect</tspan><tspan x="352" dy="5">for six months.</tspan></text>
    <text class="tiny" x="312" y="182"><tspan x="312">For every eight samples tested, three showed full</tspan><tspan x="312" dy="5">repression. Suited to every category of study,</tspan><tspan x="312" dy="5">from early screens to later dose work, and to</tspan><tspan x="312" dy="5">team updates and board presentations.</tspan></text>
  </svg>

  <!-- 17 Lab tube: rack -->
  <svg class="slide lab-rack" viewBox="0 0 478 269">
    <text class="lab-ttl" x="32" y="36">Lab Tube</text>
    <text class="sub" x="32" y="47">Put your subtitle here</text>
    <use href="#logo" x="373" y="10" width="90" height="24" class="logo-teal"/>
    <g fill="none" stroke="#bfe3f7" stroke-width="5">
      <path d="M42 118 V205 a15 15 0 0 0 30 0 V118"/><path d="M89 118 V205 a15 15 0 0 0 30 0 V118"/>
      <path d="M136 118 V205 a15 15 0 0 0 30 0 V118"/><path d="M183 118 V205 a15 15 0 0 0 30 0 V118"/>
    </g>
    <path d="M47 180 V205 a10 10 0 0 0 20 0 V180Z" fill="#2aa6e0"/>
    <path d="M94 135 V205 a10 10 0 0 0 20 0 V135Z" fill="#1e4fd8"/>
    <path d="M141 160 V205 a10 10 0 0 0 20 0 V160Z" fill="var(--violet)"/>
    <path d="M188 140 V205 a10 10 0 0 0 20 0 V140Z" fill="var(--magenta)"/>
    <rect x="34" y="195" width="220" height="5" fill="var(--seafoam)"/>
    <rect x="38" y="200" width="4" height="28" fill="var(--seafoam)"/><rect x="246" y="200" width="4" height="28" fill="var(--seafoam)"/>
    <rect x="30" y="226" width="228" height="4" fill="var(--seafoam)"/>
    <g class="label-s white center" style="font-size:3.4px">
      <circle cx="57" cy="102" r="8" fill="#2aa6e0"/><text x="57" y="103.5">37%</text>
      <circle cx="104" cy="98" r="8" fill="#1e4fd8"/><text x="104" y="99.5">90%</text>
      <circle cx="151" cy="100" r="8" fill="var(--violet)"/><text x="151" y="101.5">56%</text>
      <circle cx="198" cy="96" r="8" fill="var(--magenta)"/><text x="198" y="97.5">78%</text>
    </g>
    <g fill="#2aa6e0"><circle cx="52" cy="86" r="3"/><circle cx="98" cy="84" r="3"/><circle cx="156" cy="86" r="3"/><circle cx="203" cy="80" r="3"/></g>
    <g class="tiny center"><text x="57" y="238">Genetics</text><text x="104" y="238">Biotech</text><text x="151" y="238">Cells</text><text x="198" y="238">Therapy</text></g>
    <text class="label-s" x="293" y="114">Project Analysis</text>
    <text class="stat" x="293" y="142">99%</text>
    <text class="tiny" x="330" y="130"><tspan x="330">Of samples passed review</tspan><tspan x="330" dy="5">right before the final</tspan><tspan x="330" dy="5">release step.</tspan></text>
    <text class="tiny" x="293" y="158"><tspan x="293">For every eight batches made, we checked three for</tspan><tspan x="293" dy="5.5">purity. Suited to every category of lab report,</tspan><tspan x="293" dy="5.5">partner update and board presentation, with room</tspan><tspan x="293" dy="5.5">for short notes beneath the headline figure.</tspan><tspan x="293" dy="5.5">Keep it brief.</tspan></text>
  </svg>

  <!-- 18 Lab tube: thermometers -->
  <svg class="slide lab-gauges" viewBox="0 0 478 269">
    <text class="lab-ttl" x="32" y="36">Lab Tube</text>
    <text class="sub" x="32" y="47">Put your subtitle here</text>
    <use href="#logo" x="373" y="10" width="90" height="24" class="logo-teal"/>
    <text class="label-s" x="36" y="114">Project Analysis</text>
    <text class="stat" style="fill:var(--violet)" x="36" y="142">75%</text>
    <text class="tiny" x="72" y="130"><tspan x="72">Of samples passed review</tspan><tspan x="72" dy="5">right before the final</tspan><tspan x="72" dy="5">release step.</tspan></text>
    <text class="tiny" x="36" y="158"><tspan x="36">For every eight batches made, we checked three for</tspan><tspan x="36" dy="5.5">purity. Suited to every category of lab report,</tspan><tspan x="36" dy="5.5">partner update and board presentation, with room</tspan><tspan x="36" dy="5.5">for short notes beneath the headline figure.</tspan><tspan x="36" dy="5.5">Keep it brief.</tspan></text>
    <g fill="var(--seafoam)">
      <rect x="258" y="92" width="20" height="110" rx="4"/><circle cx="268" cy="210" r="18"/>
      <rect x="301" y="92" width="20" height="110" rx="4"/><circle cx="311" cy="210" r="18"/>
      <rect x="344" y="92" width="20" height="110" rx="4"/><circle cx="354" cy="210" r="18"/>
      <rect x="387" y="92" width="20" height="110" rx="4"/><circle cx="397" cy="210" r="18"/>
    </g>
    <rect x="263" y="180" width="10" height="25" fill="#2aa6e0"/><circle cx="268" cy="210" r="14" fill="#2aa6e0"/>
    <rect x="306" y="150" width="10" height="55" fill="#1e4fd8"/><circle cx="311" cy="210" r="14" fill="#1e4fd8"/>
    <rect x="349" y="120" width="10" height="85" fill="var(--violet)"/><circle cx="354" cy="210" r="14" fill="var(--violet)"/>
    <rect x="392" y="140" width="10" height="65" fill="var(--magenta)"/><circle cx="397" cy="210" r="14" fill="var(--magenta)"/>
    <g class="label-s white center" style="font-size:5px"><text x="268" y="212">20%</text><text x="311" y="212">50%</text><text x="354" y="212">75%</text><text x="397" y="212">60%</text></g>
    <g>
      <path d="M258 72 l10 -8 l10 8 l-10 8Z" fill="#2aa6e0"/><path d="M301 72 l10 -8 l10 8 l-10 8Z" fill="#1e4fd8"/>
      <path d="M344 72 l10 -8 l10 8 l-10 8Z" fill="var(--violet)"/><path d="M387 72 l10 -8 l10 8 l-10 8Z" fill="var(--magenta)"/>
    </g>
    <g stroke="var(--ink)" stroke-width=".8">
      <line x1="420" y1="100" x2="428" y2="100"/><line x1="420" y1="110" x2="424" y2="110"/><line x1="420" y1="120" x2="424" y2="120"/><line x1="420" y1="130" x2="424" y2="130"/><line x1="420" y1="140" x2="424" y2="140"/>
      <line x1="420" y1="150" x2="428" y2="150"/><line x1="420" y1="160" x2="424" y2="160"/><line x1="420" y1="170" x2="424" y2="170"/><line x1="420" y1="180" x2="424" y2="180"/><line x1="420" y1="190" x2="424" y2="190"/><line x1="420" y1="200" x2="428" y2="200"/>
    </g>
    <g class="tiny"><text x="432" y="102">100</text><text x="432" y="152">50</text><text x="432" y="202">0</text></g>
  </svg>

  <!-- 19 Lab tube: balance -->
  <svg class="slide lab-balance" viewBox="0 0 478 269">
    <text class="lab-ttl" x="32" y="36">Lab Tube</text>
    <text class="sub" x="32" y="47">Put your subtitle here</text>
    <use href="#logo" x="373" y="10" width="90" height="24" class="logo-teal"/>
    <rect x="163" y="92" width="152" height="8" fill="var(--seafoam)"/>
    <rect x="234" y="100" width="10" height="126" fill="var(--seafoam)"/>
    <rect x="163" y="224" width="152" height="8" fill="var(--seafoam)"/>
    <path d="M170 100 V178 a17.5 17.5 0 0 0 35 0 V100 H197 V178 a9.5 9.5 0 0 1 -19 0 V100Z" fill="var(--seafoam)"/>
    <path d="M273 100 V178 a17.5 17.5 0 0 0 35 0 V100 H300 V178 a9.5 9.5 0 0 1 -19 0 V100Z" fill="var(--seafoam)"/>
    <path d="M180 125 V178 a7.5 7.5 0 0 0 15 0 V125Z" fill="#2a7fe0"/>
    <path d="M283 140 V178 a7.5 7.5 0 0 0 15 0 V140Z" fill="var(--violet)"/>
    <g fill="none" stroke="#2aa6e0" stroke-width="1.2"><circle cx="191" cy="69" r="9"/><circle cx="178" cy="84" r="2.5"/><circle cx="181" cy="62" r="2"/></g>
    <g fill="none" stroke="var(--violet)" stroke-width="1.2"><circle cx="297" cy="78" r="8"/><circle cx="287" cy="64" r="3"/><circle cx="283" cy="72" r="2"/></g>
    <g class="tiny center" style="font-size:3.2px"><text x="191" y="70">77%</text><text x="297" y="79">53%</text></g>
    <text class="label-s" x="34" y="104">Science Analysis</text>
    <text class="stat" style="font-size:12px" x="122" y="124">77%</text>
    <text class="tiny" x="34" y="114"><tspan x="34">Suited to any kind of study</tspan><tspan x="34" dy="5">and partner review.</tspan></text>
    <text class="tiny" x="34" y="134"><tspan x="34">For every eight samples run, we checked three</tspan><tspan x="34" dy="5.5">cells. Suited to each category of lab report,</tspan><tspan x="34" dy="5.5">partner update and board presentation, with</tspan><tspan x="34" dy="5.5">space for short notes below the main figure.</tspan></text>
    <text class="label-s" x="324" y="104">Science Analysis</text>
    <text class="stat" style="font-size:12px;fill:var(--violet)" x="412" y="124">53%</text>
    <text class="tiny" x="324" y="114"><tspan x="324">Suited to any kind of study</tspan><tspan x="324" dy="5">and partner review.</tspan></text>
    <text class="tiny" x="324" y="134"><tspan x="324">For every eight samples run, we checked three</tspan><tspan x="324" dy="5.5">cells. Suited to each category of lab report,</tspan><tspan x="324" dy="5.5">partner update and board presentation, with</tspan><tspan x="324" dy="5.5">space for short notes below the main figure.</tspan></text>
  </svg>

  <!-- 20 Labtube infographic -->
  <svg class="slide lab-infographic" viewBox="0 0 478 269">
    <text class="lab-ttl" style="font-size:17px" x="35" y="32">Labtube Infographic</text>
    <text class="sub" x="35" y="46">Put your subtitle here</text>
    <use href="#logo" x="373" y="10" width="90" height="24" class="logo-teal"/>
    <g stroke="var(--line)" stroke-width="1"><line x1="168" y1="62" x2="168" y2="250"/><line x1="300" y1="62" x2="300" y2="250"/></g>
    <g fill="var(--seafoam)">
      <path d="M84 64 H124 L114 80 V170 a10 10 0 0 1 -20 0 V80Z"/>
      <path d="M212 64 H252 L242 80 V170 a10 10 0 0 1 -20 0 V80Z"/>
      <path d="M347 64 H387 L377 80 V170 a10 10 0 0 1 -20 0 V80Z"/>
    </g>
    <path d="M98 125 V168 a6 6 0 0 0 12 0 V125Z" fill="#1e4fd8"/>
    <path d="M226 138 V168 a6 6 0 0 0 12 0 V138Z" fill="#2aa6e0"/>
    <path d="M361 110 V168 a6 6 0 0 0 12 0 V110Z" fill="var(--violet)"/>
    <g stroke="var(--grey)" stroke-width=".5">
      <line x1="120" y1="82" x2="128" y2="82"/><line x1="120" y1="101" x2="128" y2="101"/><line x1="120" y1="120" x2="128" y2="120"/><line x1="120" y1="139" x2="128" y2="139"/><line x1="120" y1="158" x2="128" y2="158"/>
      <line x1="248" y1="82" x2="256" y2="82"/><line x1="248" y1="101" x2="256" y2="101"/><line x1="248" y1="120" x2="256" y2="120"/><line x1="248" y1="139" x2="256" y2="139"/><line x1="248" y1="158" x2="256" y2="158"/>
      <line x1="383" y1="82" x2="391" y2="82"/><line x1="383" y1="101" x2="391" y2="101"/><line x1="383" y1="120" x2="391" y2="120"/><line x1="383" y1="139" x2="391" y2="139"/><line x1="383" y1="158" x2="391" y2="158"/>
    </g>
    <g class="tiny" style="font-size:2.8px">
      <text x="131" y="83">100%</text><text x="131" y="102">80%</text><text x="131" y="121">60%</text><text x="131" y="140">40%</text><text x="131" y="159">20%</text>
      <text x="259" y="83">100%</text><text x="259" y="102">80%</text><text x="259" y="121">60%</text><text x="259" y="140">40%</text><text x="259" y="159">20%</text>
      <text x="394" y="83">100%</text><text x="394" y="102">80%</text><text x="394" y="121">60%</text><text x="394" y="140">40%</text><text x="394" y="159">20%</text>
    </g>
    <g class="tiny"><text x="48" y="199">Description</text><text x="180" y="199">Description</text><text x="324" y="199">Description</text></g>
    <text class="stat" style="font-size:12px" x="48" y="215">60%</text>
    <text class="stat" style="font-size:12px" x="180" y="215">40%</text>
    <text class="stat" style="font-size:12px;fill:var(--violet)" x="324" y="215">80%</text>
    <g class="tiny" style="font-size:3px">
      <text x="74" y="209"><tspan x="74">Edit it with your data,</tspan><tspan x="74" dy="4">resize the liquid</tspan></text>
      <text x="206" y="209"><tspan x="206">Edit it with your data,</tspan><tspan x="206" dy="4">resize the liquid</tspan></text>
      <text x="350" y="209"><tspan x="350">Edit it with your data,</tspan><tspan x="350" dy="4">resize the liquid</tspan></text>
      <text x="48" y="225"><tspan x="48">Short note on this result and</tspan><tspan x="48" dy="4.5">what it means for the program.</tspan></text>
      <text x="180" y="225"><tspan x="180">Short note on this result and</tspan><tspan x="180" dy="4.5">what it means for the program.</tspan></text>
      <text x="324" y="225"><tspan x="324">Short note on this result and</tspan><tspan x="324" dy="4.5">what it means for the program.</tspan></text>
    </g>
  </svg>

  <!-- 21 Icon pack -->
  <svg class="slide icon-pack" viewBox="0 0 478 269">
    <text class="label center" style="font-size:8.5px" x="239" y="36">FREE BIOCHEMISTRY ICON PACK</text>
    <g>
      <use href="#i-cell" x="27" y="57" width="30" height="30"/><use href="#i-person" x="71" y="57" width="30" height="30"/><use href="#i-molecule" x="116" y="57" width="30" height="30"/><use href="#i-person" x="161" y="57" width="30" height="30"/><use href="#i-flask" x="205" y="57" width="30" height="30"/>
      <use href="#i-helix" x="250" y="57" width="30" height="30"/><use href="#i-molecule" x="294" y="57" width="30" height="30"/><use href="#i-cell" x="339" y="57" width="30" height="30"/><use href="#i-helix" x="384" y="57" width="30" height="30"/><use href="#i-person" x="428" y="57" width="30" height="30"/>
      <use href="#i-flask" x="27" y="127" width="30" height="30"/><use href="#i-molecule" x="71" y="127" width="30" height="30"/><use href="#i-helix" x="116" y="127" width="30" height="30"/><use href="#i-person" x="161" y="127" width="30" height="30"/><use href="#i-cell" x="205" y="127" width="30" height="30"/>
      <use href="#i-molecule" x="250" y="127" width="30" height="30"/><use href="#i-person" x="294" y="127" width="30" height="30"/><use href="#i-flask" x="339" y="127" width="30" height="30"/><use href="#i-cell" x="384" y="127" width="30" height="30"/><use href="#i-helix" x="428" y="127" width="30" height="30"/>
      <use href="#i-molecule" x="27" y="197" width="30" height="30"/><use href="#i-helix" x="71" y="197" width="30" height="30"/><use href="#i-cell" x="116" y="197" width="30" height="30"/><use href="#i-flask" x="161" y="197" width="30" height="30"/><use href="#i-person" x="205" y="197" width="30" height="30"/>
      <use href="#i-flask" x="250" y="197" width="30" height="30"/><use href="#i-helix" x="294" y="197" width="30" height="30"/><use href="#i-person" x="339" y="197" width="30" height="30"/><use href="#i-molecule" x="384" y="197" width="30" height="30"/><use href="#i-cell" x="428" y="197" width="30" height="30"/>
    </g>
  </svg>

</main>
</body>
</html>
```